Business Card Design

We like to use greens as you will see in our logo (but not TOO much green). We are a Dental Clinic in a somewhat eccentric community. We do not like the dated sharp designs which we see many dentists use. We're looking for something bright and fresh while still maintaining the integrity of the profession. Elegance is not necessarily what we are going for... we need for the design to be "mature" but also up-lifting.

See our logo.
Updates

Project Deadline Extended
Reason: We have 5 designs which we like. But we'd like to see a few more before committing to a design.

Project Deadline Extended
Reason: We are awaiting revisions to this project. We are still welcoming designs while we wait to see if designers are able to provide to us the revisions we require in order to proceed with a selection.

Target Market(s)

Younger families - ages late 20's to early 40's

Industry/Entity Type

Business

Contact Information for Business Card

Marlow T. Venn DDS 2737 S. Fennimore Ave. Ste. 8 Royal Oak, MI 48059 (248)555-0174 FX (248)555-0189 info@BrightwaveDentalMi.example BrigthwaveDentalMi.example on the back of the card we need an appointment reminder (For____ Date___ Time____) with "If you are unable to keep your appointment, kindly give 48 hours notice" at the bottom. No use of teeth in the design. DOUBLE SIDED DESIGN

Requirements
Should not have
• The use of pictures of teeth

```html
<!DOCTYPE html>
<html lang="en">
<head>
<meta charset="utf-8">
<title>Brightwave Dental Care – Business Card</title>
<link href="https://fonts.googleapis.com/css2?family=Lato:wght@400;700;900&display=swap" rel="stylesheet">
<style>
  :root {
    --green: #1e8f45;
    --green-dark: #17733a;
    --lime: #8cc63f;
    --leaf: #5cb247;
    --ink: #1c1c1c;
    --rule: #8a8a8a;
    --paper: #ffffff;
    --backdrop: #e9ebea;
  }
  * { box-sizing: border-box; margin: 0; padding: 0; }
  html, body {
    width: 1200px; height: 926px; overflow: hidden;
    background: var(--backdrop);
    font-family: "Lato", Arial, sans-serif;
    color: var(--ink);
  }
  .canvas { position: relative; width: 1200px; height: 926px; }

  .card {
    position: absolute; top: 308px;
    width: 540px; height: 309px;
    background: var(--paper);
    overflow: hidden;
    box-shadow: 0 6px 18px rgba(0,0,0,.18);
  }
  .card--front { left: 40px; }
  .card--back { left: 620px; }

  /* Front */
  .brand {
    position: absolute; left: 34px; top: 26px;
    display: flex; align-items: center; gap: 10px;
  }
  .brand__dot { width: 22px; height: 22px; border-radius: 50%; background: var(--leaf); }
  .brand__name {
    font-weight: 700; font-size: 22px; line-height: 1.05; color: var(--green);
  }
  .person {
    position: absolute; left: 34px; top: 106px;
    font-size: 21px; font-weight: 400; letter-spacing: .2px;
  }
  .person__title { color: var(--green); font-size: 15px; }
  .contacts {
    position: absolute; left: 34px; top: 140px;
    list-style: none; font-size: 13.5px; line-height: 19.5px;
  }
  .contacts li { display: flex; align-items: center; gap: 8px; }
  .contacts svg { width: 13px; height: 13px; fill: var(--green); flex: none; }
  .band--address {
    position: absolute; left: 0; right: 0; bottom: 0; height: 54px;
    background: var(--green);
    display: flex; align-items: center; gap: 10px; padding-left: 24px;
    color: #fff; font-weight: 700; font-size: 15px; letter-spacing: 2.4px;
  }
  .band--address svg { width: 14px; height: 20px; fill: #fff; flex: none; }
  .accent {
    position: absolute; right: 0; top: 0; width: 190px; height: 255px;
    background: radial-gradient(circle at 45% 45%, var(--leaf) 0%, var(--lime) 55%, #c5e29a 100%);
  }

  /* Back */
  .appointment__title {
    position: absolute; left: 0; right: 0; top: 30px;
    text-align: center; font-weight: 700; font-size: 17px; letter-spacing: 1.6px;
  }
  .field {
    position: absolute; left: 36px; right: 36px;
    display: flex; align-items: flex-end; gap: 10px; font-size: 13px;
  }
  .field--date { top: 68px; }
  .field--time { top: 102px; }
  .field__line { flex: 1; border-bottom: 1px solid var(--rule); height: 14px; }
  .band--notice {
    position: absolute; left: 0; right: 0; bottom: 0; height: 138px;
    background: var(--green);
    color: #fff; text-align: center;
    display: flex; flex-direction: column; justify-content: center;
    font-size: 17px; line-height: 25px;
  }
  .band--notice strong { font-weight: 700; font-size: 18px; }
</style>
</head>
<body>
<main class="canvas">

  <section class="card card--front" aria-label="Business card front">
    <div class="brand">
      <span class="brand__dot"></span>
      <span class="brand__name">Brightwave<br>Dental Care</span>
    </div>

    <p class="person">Marlow T. Venn <span class="person__title">-DDS</span></p>

    <ul class="contacts">
      <li><svg viewBox="0 0 24 24"><path d="M6.6 10.8a15.1 15.1 0 0 0 6.6 6.6l2.2-2.2a1 1 0 0 1 1-.25 11.4 11.4 0 0 0 3.6.57 1 1 0 0 1 1 1V20a1 1 0 0 1-1 1A17 17 0 0 1 3 4a1 1 0 0 1 1-1h3.5a1 1 0 0 1 1 1c0 1.25.2 2.45.57 3.57a1 1 0 0 1-.25 1z"/></svg>(248)555-0174</li>
      <li><svg viewBox="0 0 24 24"><path d="M6 2h12v6H6zM3 9h18v9h-3v4H6v-4H3zm5 7v4h8v-4z"/></svg>(248)555-0189</li>
      <li><svg viewBox="0 0 24 24"><path d="M2 3h20v14H13v2h4v2H7v-2h4v-2H2zm2 2v10h16V5z"/></svg>BrigthwaveDentalMi.example</li>
      <li><svg viewBox="0 0 24 24"><path d="M2 4h20v16H2zm2 2v.5l8 6 8-6V6zm0 3v9h16V9l-8 6z"/></svg>info@BrightwaveDentalMi.example</li>
    </ul>

    <div class="accent" role="img" aria-label="Decorative cluster of overlapping translucent green circles"></div>

    <footer class="band--address">
      <svg viewBox="0 0 14 20"><path d="M7 0a7 7 0 0 0-7 7c0 5.2 7 13 7 13s7-7.8 7-13a7 7 0 0 0-7-7zm0 9.5A2.5 2.5 0 1 1 7 4.5a2.5 2.5 0 0 1 0 5z"/></svg>
      2737 S. Fennimore Ave. Ste. 8 Royal Oak, MI 48059
    </footer>
  </section>

  <section class="card card--back" aria-label="Business card back">
    <h2 class="appointment__title">APPOINTMENT</h2>
    <div class="field field--date"><span>Date:</span><span class="field__line"></span></div>
    <div class="field field--time"><span>Time:</span><span class="field__line"></span></div>
    <footer class="band--notice">
      <span>If you are unable to keep your appointment</span>
      <strong>kindly give 48 hours notice</strong>
    </footer>
  </section>

</main>
</body>
</html>
```